I want an upgrade / face-lift to the all the pages and sections of the current website at vorenta.net. I am a developer but not a designer.

The website layout does not need to stay the same. Only the text, buttons, links, etc, need to stay the same. Logo can also be changed or altered.

1) Header
* Logo
* Tagline - Friends of the Messianic Community in Israel
* Short explanation - Vorenta.net aggregates new links from 113 websites of the Messianic Community in Israel. Learn more
* Login button
* Language Links (or picker) - English, Hebrew, Chinese (this currently isn't on Vorenta.net)

2) Nav Bar - no dropdowns
* Newsfeed
* Israel Directory
* International Directory
* Product Directory
* Website Directory

3) Sidebar
* Text - Sign up to Vorenta.net to receive a weekly email of new articles and videos from the Messianic community in Israel.
* Sign up button
* Brixo Ads or other Ads

4) List of Newsfeed links - (this is the main content of the homepage. Note the links go to other websites. It's not blog entries)
* Image
* Link Title
* website
* author (optional)
* date
* short description of link (optional)

5) Directory (Israel, International, Product)
* Search / Filter Bar (left vertical or horizontal ???)
* title - Israel Directory
* # of results
* A-Z
Partial for each organization
* logo
* first line - Link Name
* second link - type, city, language, area
* number of views
* description

6) Website Directory - page that lists all the websites that we crawl and gather links.
* needs upgrade / facelift

7) Organization Profile Page - click on http://vorenta.net/shalev-gate-fellowship as an example.
* all details as in list of directory, plus
* Meeting details
* contact details
* Donation details
* Donation link more prominent

8) Register Page
* include all details as on http://vorenta.net/register

9) Login Page
* include all details as on http://vorenta.net/login

10) About / FAQ / Contact pages
* include all details as on http://vorenta.net/about
* include all details as on http://vorenta.net/faq
* include all details as on http://vorenta.net/contact

11) Footer
* * include all details as on as website
About | Newsfeed | Israel Directory | International Directory | Product Directory | Website Directory | Contact
©2006–2013 Vorenta.net All rights reserved
Vorenta is a Hebrew word that means "community" or "congregation"

12) Bonus - Email Newsletter Design
* I want to send out 5 -10 new newsfeed links each weeks
* It should be similar to the newsfeed page, but for e-newsletters. I read that the css must for different and tables are preferred about for email.

The following pages appear for logged in users only
13) List of Ads
14) List of Events
15) Ad Single Page
16) Event Single Page
17) Edit Ad Form
18) Edit Event Form
19) Edit Organization Form
20) Edit User Information Form

Reason: First project. I originally entered 2 days, but am extending to 10 days.

I removed the requirement to delivery HTML/CSS and I static design of all pages is acceptable to win the project.  This is my first project and I wasn't aware that PixelHarbor focuses on static design and not HTML/CSS code.

Every designer essentially used the exact same "layout" that I currently have at vorenta.net and gave it a small "facelift".  I guess my wording in the brief of the word 'facelift' was not totally accurate.  The navbar / header layout does not need to stay the same.  I would appreciate to see different options such as the navbar at the top (like www.trendolix.net) or all one color on the header (like www.gbx.net) or making the logo all white and putting it inside the blue navbar (like trendolix.net).  Just some ideas that I had.

I am willing to make the project guaranteed but most of the designs are very close to what I have now.  

Note, any ideas / graphics / images / icons that show the visitor that the website is related to Israel would be helpful.

Reason: Not enough designs received

The project is now guaranteed‎.  I hope this encourages more designers to submit and to be creative.  I look forward to seeing more designs.

I'm interested in having a background on the left and right sides for larger screens.  For an example, see http://fieldsidetally.net/

I would like to have a faded image of the Israeli flag or a creative variation of it.

This website has a background image on the right-left sides that fades as you go down

I'm looking to use the space and the right-left to give the user at a quick glance that the website deals with Israel, community, Messianic/Christian, etc.

Another style that looks good is that white/gray such as http://www.filmquillnotes.net/ and https://vestly.io/

I'm interested to see how to block out difference sections with small color variations.

Reason: some designers request that I extend since they just accepted invitation

Another design that I like.  http://gigbarn.net/

Important change.  I want the newsfeed to look like a newsfeed. Right now, it looks like a blog site.  It's not obvious that articles are from other websites in the community.  I uploaded on the brief of clipvane's feed.  It shows the a small thumbnail (16x16 or 32x32) and then user name (it my case organization name or website name) on the upper left corner above the main image. 

On the header on want to change the wording on order.  

Top row -
Vorenta (logo in big) means community in Hebrew (in small letters) 

Next row (different background color)
The Messianic Community in Israel

Next row (different background color and smaller font)
Vorenta.net aggregates new links from 100+ websites of the Messianic Community in Israel. Learn more

I uploaded a jpg file with a new header rather than what is currently on vorenta.net

Target Market(s)

Christian around the world who love Israel

Industry/Entity Type

Events

Requirements
Must have
• responsive design to be readable on mobile devices
white / gray / blue theme
Zapto-style / portal website
Nice to have
• Bootstrap 3 of Foundation
Flat-UI (also not necessary, but I like it)
Graphics, icons, etcs, related to Israel
Passion, excellence, effort and attention to details :-)
Should not have
• dark background
too much fanciness or animations

```html
<!DOCTYPE html>
<html lang="en">
<head>
<meta charset="utf-8">
<title>Vorenta.net — Newsfeed</title>
<link rel="stylesheet" href="https://fonts.googleapis.com/css2?family=Open+Sans:wght@400;600;700;800&display=swap">
<style>
:root{
  --navy:#0d1b3d;
  --blue:#1f5fd6;
  --link:#2a6bd8;
  --text:#1d2433;
  --muted:#7b8494;
  --line:#e3e6eb;
  --panel:#f4f5f7;
  --white:#ffffff;
  --ad-blue:#1565c0;
  --ad-orange:#f58a1f;
  --ad-red:#d9261c;
}
*{box-sizing:border-box;margin:0;padding:0}
html,body{width:776px;height:1200px;overflow:hidden}
body{font-family:"Open Sans",Arial,sans-serif;color:var(--text);background:var(--white);position:relative}
a{color:inherit;text-decoration:none}

.top-strip{height:30px;background:var(--navy);color:#cfd6e6;font-size:9.5px;display:flex;align-items:center;padding-left:90px}
.top-strip .learn{color:#7fb0ff;margin-left:4px}

.masthead{height:58px;display:flex;align-items:center;justify-content:space-between;padding:0 83px 0 90px}
.brand{font-size:22px;font-weight:800;color:var(--blue);letter-spacing:-.3px}
.masthead-right{display:flex;align-items:center;gap:12px}
.tagline{font-size:10px;color:var(--text)}
.btn-login{background:var(--blue);color:var(--white);font-size:10px;font-weight:600;padding:5px 14px;border-radius:2px}

.main-nav{height:36px;background:var(--blue);display:flex;align-items:center;padding-left:90px;gap:22px}
.main-nav a{color:var(--white);font-size:11px;font-weight:600}

.page{display:flex;gap:14px;padding:14px 83px 0 90px}
.feed{width:446px}
.feed-item{display:flex;gap:12px;height:114px;padding:8px 10px;border-bottom:1px solid var(--line);background:var(--panel)}
.feed-item:nth-child(even){background:var(--white)}
.thumb{width:104px;height:80px;flex:none;border-radius:2px}
.feed-body{padding-top:30px;min-width:0}
.feed-title{font-size:10px;font-weight:700;line-height:1.3;white-space:nowrap}
.feed-meta{font-size:8.5px;color:var(--muted);margin-top:3px}
.feed-meta .source{color:var(--link)}

.sidebar{width:144px}
.signup-head{font-size:10px;color:var(--link);margin-top:4px}
.signup-text{font-size:8px;color:var(--muted);line-height:1.4;margin:6px 0 8px}
.btn-signup{display:inline-block;background:var(--blue);color:var(--white);font-size:10.5px;font-weight:700;padding:5px 14px;border-radius:2px}

.ad{margin-top:14px;width:144px;overflow:hidden}
.ad-host{height:424px;background:var(--ad-blue);color:var(--white);text-align:center;padding-top:10px}
.ad-host .ad-brand{font-size:22px;font-weight:800}
.ad-host .ad-line{font-size:10.5px;font-weight:600;line-height:1.3;margin:6px 8px}
.ad-host .ad-big{font-size:17px;font-weight:800;margin:8px 0}
.ad-host .ad-art{height:60px;margin:8px 14px;border-radius:2px}
.ad-host .ad-price{background:var(--ad-orange);margin:12px 10px 0;padding:8px 4px;font-size:14px;font-weight:800}
.ad-dogs{height:406px;border:2px solid var(--ad-red);background:var(--white);text-align:center;padding-top:8px}
.ad-dogs .ad-tag{font-size:15px;font-weight:800;color:var(--ad-red);line-height:1.1}
.ad-dogs .ad-head{background:var(--ad-orange);color:var(--white);font-size:14px;font-weight:800;margin:6px 8px;padding:6px;line-height:1.15}
.ad-dogs .ad-price{font-size:28px;font-weight:800;color:var(--ad-red)}
.ad-dogs .ad-art{height:130px;margin:6px 14px;border-radius:2px}
.ad-dogs .ad-buy{display:inline-block;background:var(--ad-red);color:var(--white);font-size:13px;font-weight:800;padding:7px 16px;border-radius:16px;margin-top:4px}
.ad-dogs .ad-url{font-size:7.5px;color:var(--muted);margin-top:8px}

.pager{position:absolute;top:1058px;left:268px;display:flex;gap:5px}
.pager span{width:18px;height:18px;border:1px solid var(--line);font-size:8px;display:flex;align-items:center;justify-content:center;color:var(--muted);background:var(--white)}
.pager .current{background:var(--navy);color:var(--white);border-color:var(--navy)}
.pager .gap{border:none}

.site-footer{position:absolute;top:1136px;left:0;width:776px;height:64px;background:var(--navy);color:#c7cee0;padding:16px 83px 0 90px}
.footer-links{display:flex;gap:10px;font-size:8.5px}
.footer-links span{color:#56617c}
.copyright{font-size:8px;margin-top:12px;color:#8f98ad}
.social{position:absolute;right:83px;top:16px;display:flex;gap:5px}
.social i{width:11px;height:11px;background:#8f98ad;border-radius:2px;display:block}
</style>
</head>
<body>

<div class="top-strip">Vorenta.net aggregates new links from 113 websites of the Messianic Community in Israel. <a class="learn" href="#">Learn more</a></div>

<header class="masthead">
  <a class="brand" href="#">Vorenta</a>
  <div class="masthead-right">
    <span class="tagline">Friends of the Messianic Community in Israel</span>
    <a class="btn-login" href="#">Login</a>
  </div>
</header>

<nav class="main-nav">
  <a href="#">Newsfeed</a><a href="#">Israel Directory</a><a href="#">International Directory</a><a href="#">Product Directory</a><a href="#">Website Directory</a>
</nav>

<div class="page">
  <main class="feed">
    <article class="feed-item">
      <div class="thumb" role="img" aria-label="Photo of a man speaking" style="background:linear-gradient(135deg,#8a7565,#3d3a3e)"></div>
      <div class="feed-body"><h3 class="feed-title">Kestrel Prayer Circle Prayer Points - 20 September 2013</h3><p class="feed-meta"><span class="source">arvelo.org.il</span> | September 20, 2013</p></div>
    </article>
    <article class="feed-item">
      <div class="thumb" role="img" aria-label="Photo of a sukkah booth" style="background:linear-gradient(135deg,#9bb07a,#6a7350)"></div>
      <div class="feed-body"><h3 class="feed-title">Sukkot 5774: Build Your Booth and Dwell in It</h3><p class="feed-meta"><span class="source">tovimblog.com</span> | September 18, 2013</p></div>
    </article>
    <article class="feed-item">
      <div class="thumb" role="img" aria-label="Video still of a speaker" style="background:linear-gradient(135deg,#2b4f9e,#c23a3a)"></div>
      <div class="feed-body"><h3 class="feed-title">Why didn't I Name Names?</h3><p class="feed-meta"><span class="source">shoravoice.org</span> | September 18, 2013</p></div>
    </article>
    <article class="feed-item">
      <div class="thumb" role="img" aria-label="Photo of sorted paper files" style="background:linear-gradient(135deg,#d9d3c8,#9c948a)"></div>
      <div class="feed-body"><h3 class="feed-title">Time to Start Sorting</h3><p class="feed-meta"><span class="source">kelmora.org</span> | September 17, 2013</p></div>
    </article>
    <article class="feed-item">
      <div class="thumb" role="img" aria-label="Podcast episode artwork" style="background:linear-gradient(135deg,#c9a23a,#5d4a22)"></div>
      <div class="feed-body"><h3 class="feed-title">[Podcast] Yom Kippur, Televangelists and Syria Update</h3><p class="feed-meta"><span class="source">shoravoice.org</span> | September 17, 2013</p></div>
    </article>
    <article class="feed-item">
      <div class="thumb" role="img" aria-label="Photo of a festive gathering" style="background:linear-gradient(135deg,#d69a9a,#7a5a6e)"></div>
      <div class="feed-body"><h3 class="feed-title">A Feast Of Rejoicing!</h3><p class="feed-meta"><span class="source">ardenline.org</span> | September 16, 2013</p></div>
    </article>
    <article class="feed-item">
      <div class="thumb" role="img" aria-label="Photo of a wooden booth outdoors" style="background:linear-gradient(135deg,#8c6a45,#4a5a3a)"></div>
      <div class="feed-body"><h3 class="feed-title">A Feast Of Rejoicing!</h3><p class="feed-meta"><span class="source">ardenline.org</span> | September 16, 2013</p></div>
    </article>
    <article class="feed-item">
      <div class="thumb" role="img" aria-label="Photo of banknotes" style="background:linear-gradient(135deg,#c8d0c0,#7d8a78)"></div>
      <div class="feed-body"><h3 class="feed-title">Televangelists Abusing the Day of Atonement — from Kippur</h3><p class="feed-meta"><span class="source">shoravoice.org</span> | September 15, 2013</p></div>
    </article>
  </main>

  <aside class="sidebar">
    <p class="signup-head">Sign up to Vorenta.net</p>
    <p class="signup-text">To receive a weekly email of new articles and videos from the Messianic community in Israel.</p>
    <a class="btn-signup" href="#">Sign Up</a>

    <div class="ad ad-host">
      <div class="ad-brand">Hostrane</div>
      <div class="ad-big">13 Datacenters</div>
      <div class="ad-art" role="img" aria-label="World map illustration" style="background:linear-gradient(#3f86d6,#1f5aa8)"></div>
      <div class="ad-line">We have locations where you need them</div>
      <div class="ad-big">Auto Healing</div>
      <div class="ad-line">With the cloud, hardware failures are a thing of the past</div>
      <div class="ad-big">Auto Scaling</div>
      <div class="ad-line">Dynamically add resources on the fly</div>
      <div class="ad-price">Starting at just $20 a month</div>
    </div>

    <div class="ad ad-dogs">
      <div class="ad-tag">SPECIAL OFFER</div>
      <div class="ad-head">25 Food Recipes for Dogs Plus Bonuses</div>
      <div class="ad-price">$39.97</div>
      <div class="ad-art" role="img" aria-label="Recipe book cover with a dog" style="background:linear-gradient(135deg,#f2c66b,#c9772f)"></div>
      <a class="ad-buy" href="#">BUY NOW!</a>
      <div class="ad-url">PawPantryRecipes.net</div>
    </div>
  </aside>
</div>

<nav class="pager" aria-label="Pages">
  <span>‹</span><span>2</span><span>3</span><span>4</span><span class="current">5</span><span>6</span><span>7</span><span class="gap">…</span><span>33</span><span>44</span><span>55</span><span>›</span>
</nav>

<footer class="site-footer">
  <div class="footer-links">
    <a href="#">Newsfeed</a><span>|</span><a href="#">Israel Directory</a><span>|</span><a href="#">International Directory</a><span>|</span><a href="#">Product Directory</a><span>|</span><a href="#">Website Directory</a>
  </div>
  <p class="copyright">©2006–2013 Vorenta.net All rights reserved</p>
  <div class="social"><i></i><i></i><i></i><i></i><i></i></div>
</footer>

</body>
</html>
```